Media and Film Company Needs a New Website

We produce highly stylized commercials and film pieces for our clients. We also produce live events, both corporate and theatrical. Looking for a site that can show off our client videos - have a polished way to show off our team, and be able to create pages to highlight our clients and give a full overview of our project/process with them. We design simple website for some of our clients - so we are very wordpress familiar, and would like something that doesn't feel like a template.

Target Market(s)

content creators, creative directors, production teams, marketing agencies

Industry/Entity Type

Film Production

Number of Pages Required

4 page

Font styles to use
Sans Serif

Requirements
Must have
• slick looking video embed (from YT or Vimeo)
• project pages - client snapshot (what we did for them, how we did it)
• nice landing page, have our company video reel on the page
• testimonials
• contact page
• ability to have photos as a background if we want
Nice to have
• polished clean look - look to our logo colors and linear elements
• we produce very stylized videos for our clients and our website should reflect that
Should not have
• template look or feel to it- please bring your flare to the project!
• take a look at our current site - zantorvo.com we need a better way to highlight our work and our clients

```html
<!DOCTYPE html>
<html lang="en">
<head>
<meta charset="utf-8">
<title>Zantorvo Media &amp; Entertainment</title>
<link href="https://fonts.googleapis.com/css2?family=Montserrat:wght@400;500;600;700;800&family=Open+Sans:wght@400;600;700&display=swap" rel="stylesheet">
<style>
:root{
  --blue:#1e9ad6;
  --cyan:#00aeef;
  --navy:#1b6fae;
  --dark:#222427;
  --darker:#1a1b1d;
  --ink:#333;
  --muted:#666;
  --light:#eeeeee;
  --yellow:#f4c51c;
  --white:#fff;
}
*{box-sizing:border-box;margin:0;padding:0}
html,body{width:1200px;height:3888px;overflow:hidden}
body{position:relative;font-family:"Open Sans",Arial,sans-serif;color:var(--ink);background:var(--white)}
.abs{position:absolute}
.ph{position:absolute}

/* header */
.site-header{position:absolute;left:0;top:0;width:1200px;height:98px;background:var(--blue)}
.brand-panel{position:absolute;left:0;top:0;height:98px;width:1200px}
.brand{position:absolute;left:250px;top:30px;font-family:"Montserrat",sans-serif;font-weight:800;font-size:34px;color:var(--dark);letter-spacing:1px;line-height:1}
.brand-sub{position:absolute;left:282px;top:68px;font-family:"Montserrat",sans-serif;font-weight:600;font-size:11px;color:var(--dark);letter-spacing:1.5px}
.phone-label{position:absolute;left:700px;top:14px;color:#fff;font-size:11px;font-weight:600;text-align:right;width:110px}
.phone-num{position:absolute;left:690px;top:30px;color:#fff;font-size:15px;font-weight:700;width:120px;text-align:right}
.social-head{position:absolute;left:822px;top:16px;display:flex;gap:8px}
.social-head span{width:26px;height:26px;border:2px solid #fff;border-radius:50%}
.main-nav{position:absolute;left:546px;top:66px;display:flex;gap:22px;font-family:"Montserrat",sans-serif;font-size:12px;font-weight:600;color:#fff}
.main-nav a{color:#fff;text-decoration:none}
.main-nav a.active{border-bottom:2px solid #fff;padding-bottom:4px}

/* hero video */
.hero{position:absolute;left:0;top:98px;width:1200px;height:571px;background:radial-gradient(ellipse at 50% 35%,#5d6066 0%,#2b2d31 45%,#141518 100%)}
.player-bar{position:absolute;left:36px;top:514px;width:1130px;height:30px}
.play-btn{position:absolute;left:0;top:0;width:48px;height:30px;background:var(--blue);border-radius:2px}
.progress{position:absolute;left:88px;top:13px;width:1000px;height:5px;background:#555a62}
.progress i{position:absolute;left:0;top:0;width:470px;height:5px;background:var(--blue)}
.side-tools{position:absolute;left:1138px;top:24px;display:flex;flex-direction:column;gap:6px}
.side-tools span{width:46px;height:38px;background:var(--blue);border-radius:3px;color:#fff;font-size:8px;text-align:center;padding-top:24px}

/* what we do */
.services{position:absolute;left:0;top:669px;width:1200px;height:446px;background:linear-gradient(#f6f6f6,#d8d8d8)}
.section-title{font-family:"Montserrat",sans-serif;font-size:40px;font-weight:500;text-align:center;color:var(--blue);letter-spacing:1px}
.section-title b{font-weight:800}
.services .section-title{position:absolute;left:0;top:82px;width:1200px;color:var(--cyan)}
.lead{position:absolute;left:370px;width:460px;text-align:center;font-size:10px;line-height:14px;color:#555}
.service{position:absolute;top:188px;width:150px;text-align:center}
.service .ring{width:130px;height:130px;margin:0 auto;border-radius:50%;background:var(--white);border:9px solid var(--blue);display:flex;align-items:center;justify-content:center}
.service .ring svg{width:66px;height:66px}
.service p{margin-top:10px;font-family:"Montserrat",sans-serif;font-size:14px;line-height:16px;color:#666}
.service p b{color:#333;font-weight:700;font-size:15px}

/* portfolio */
.portfolio-title{position:absolute;left:0;top:1170px;width:1200px;color:var(--blue);font-weight:800}
.tile{position:absolute}
.link-tile{background:var(--blue);display:flex;align-items:center;justify-content:center}
.link-tile span{width:92px;height:92px;border-radius:50%;background:#fff;display:flex;align-items:center;justify-content:center}

/* press */
.press{position:absolute;left:0;top:2216px;width:1200px;height:778px;background:linear-gradient(#ededed,#c9c9c9)}
.press .section-title{position:absolute;left:0;top:80px;width:1200px;color:var(--blue);font-weight:800}
.card{position:absolute;background:#fff;box-shadow:0 1px 3px rgba(0,0,0,.2)}
.meta{font-size:8px;color:#333;display:flex;justify-content:space-between;font-weight:600}
.meta em{font-style:normal;color:#d33}
.card h3{font-family:"Montserrat",sans-serif;font-size:14px;line-height:16px;font-weight:500;color:var(--blue);margin:8px 0 6px}
.card h3 b{font-weight:700}
.card p{font-size:8px;line-height:11px;color:#888}
.card-foot{position:absolute;left:10px;right:10px;bottom:10px;height:22px}
.share{position:absolute;left:0;top:0;width:22px;height:22px;background:#222;border-radius:2px}
.more{position:absolute;right:0;top:1px;width:96px;height:20px;border:1px solid #333;font-size:9px;font-weight:600;text-align:center;line-height:18px}

/* testimonials */
.testimonials{position:absolute;left:0;top:2994px;width:1200px;height:492px;background:linear-gradient(#1aa6e2,#0c95d3)}
.testimonials h2{position:absolute;top:78px;width:1200px;text-align:center;font-family:"Montserrat",sans-serif;font-weight:800;font-size:40px;color:#fff}
.avatar{position:absolute;left:560px;top:154px;width:80px;height:80px;border-radius:50%;border:4px solid #fff;background:linear-gradient(#c29a86,#5a4a44)}
.t-name{position:absolute;top:253px;width:1200px;text-align:center;font-family:"Montserrat",sans-serif;font-weight:700;font-size:15px;color:#fff}
.t-role{position:absolute;top:274px;width:1200px;text-align:center;font-size:10px;font-style:italic;color:#dff3fc}
.t-quote{position:absolute;left:340px;top:310px;width:520px;text-align:center;font-size:12px;line-height:17px;color:#fff}
.dots{position:absolute;left:580px;top:436px;display:flex;gap:6px}
.dots i{width:8px;height:8px;border-radius:50%;border:1px solid #fff}
.dots i.on{background:#fff}

/* newsletter */
.newsletter{position:absolute;left:0;top:3486px;width:1200px;height:135px;background:var(--yellow)}
.newsletter h2{position:absolute;left:314px;top:22px;font-family:"Montserrat",sans-serif;font-weight:800;font-size:28px;color:#222}
.nl-input{position:absolute;left:306px;top:73px;width:350px;height:36px;background:#fff;border-radius:18px;font-size:9px;color:#999;padding:12px 16px}
.nl-send{position:absolute;left:546px;top:73px;width:110px;height:36px;background:var(--blue);border-radius:18px;color:#fff;font-family:"Montserrat",sans-serif;font-weight:700;font-size:15px;text-align:center;line-height:36px}
.nl-social{position:absolute;left:762px;top:40px;display:flex;gap:10px}
.nl-social i{width:40px;height:40px;border-radius:50%}

/* footer */
.site-footer{position:absolute;left:0;top:3621px;width:1200px;height:241px;background:var(--dark)}
.f-col{position:absolute;top:40px;color:#ccc;font-size:9px;line-height:14px}
.f-col h4{font-family:"Montserrat",sans-serif;font-size:15px;font-weight:700;color:#fff;margin-bottom:14px;letter-spacing:.5px}
.f-col b{color:#fff}
.f-links li{list-style:none;padding:4px 0;border-bottom:1px solid #3a3c40;font-size:9px;color:#ddd}
.f-links li::before{content:"";display:inline-block;width:5px;height:5px;background:var(--blue);margin-right:8px}
.post{display:flex;gap:10px;align-items:center;margin-bottom:16px}
.post i{width:40px;height:40px;border-radius:50%;border:2px solid #fff;flex:none}
.copyright{position:absolute;left:0;top:3862px;width:1200px;height:26px;background:var(--blue);color:#fff;font-size:9px;padding:8px 250px}
</style>
</head>
<body>

<header class="site-header">
  <svg class="abs" style="left:0;top:0" width="480" height="98"><polygon points="0,0 480,0 450,98 0,98" fill="#fff"/></svg>
  <div class="brand">ZANTORVO</div>
  <div class="brand-sub">&amp; ENTERTAINMENT</div>
  <div class="phone-label">Phone Number</div>
  <div class="phone-num">+1 555 014 2870</div>
  <div class="social-head"><span></span><span></span><span></span><span></span></div>
  <nav class="main-nav">
    <a class="active">HOME</a><a>PORTFOLIO</a><a>ABOUT ZANTORVO</a><a>TESTIMONIALS</a><a>PRESS</a><a>CONTACT US</a>
  </nav>
</header>

<section class="hero" role="img" aria-label="Company video reel: dusk silhouette of a monument and trees">
  <div class="side-tools"><span>LIKE</span><span>SAVE</span><span>SHARE</span></div>
  <div class="player-bar">
    <div class="play-btn"><svg width="48" height="30"><polygon points="20,9 30,15 20,21" fill="#fff"/></svg></div>
    <div class="progress"><i></i></div>
    <svg class="abs" style="left:1062px;top:9px" width="60" height="12"><rect x="0" y="3" width="22" height="5" fill="#888"/><rect x="34" y="0" width="10" height="10" fill="none" stroke="#aaa"/><rect x="48" y="0" width="10" height="10" fill="none" stroke="#aaa"/></svg>
  </div>
</section>

<section class="services" aria-label="What we do">
  <h2 class="section-title">WHAT <b>WE DO</b></h2>
  <p class="lead" style="top:130px">We craft stylized commercials, film pieces and live events for brands and stages alike. Every project starts with a story, is shaped by a focused crew and ends with work that people remember and share across every screen.</p>
  <div class="service" style="left:322px"><div class="ring"><svg viewBox="0 0 66 66"><circle cx="33" cy="33" r="24" fill="none" stroke="#1e9ad6" stroke-width="5"/><circle cx="33" cy="20" r="5" fill="#1e9ad6"/><circle cx="33" cy="46" r="5" fill="#1e9ad6"/><circle cx="20" cy="33" r="5" fill="#1e9ad6"/><circle cx="46" cy="33" r="5" fill="#1e9ad6"/></svg></div><p>FILM &amp; MEDIA<br><b>PRODUCTION</b></p></div>
  <div class="service" style="left:458px"><div class="ring"><svg viewBox="0 0 66 66"><polygon points="20,14 36,10 44,30 28,34" fill="#1e9ad6"/><line x1="32" y1="32" x2="32" y2="52" stroke="#1e9ad6" stroke-width="4"/><rect x="20" y="52" width="24" height="5" fill="#1e9ad6"/></svg></div><p>LIVE<br><b>PRODUCTION</b></p></div>
  <div class="service" style="left:594px"><div class="ring"><svg viewBox="0 0 66 66"><rect x="25" y="8" width="16" height="30" rx="8" fill="#1e9ad6"/><path d="M18 30a15 15 0 0 0 30 0" fill="none" stroke="#1e9ad6" stroke-width="4"/><line x1="33" y1="45" x2="33" y2="56" stroke="#1e9ad6" stroke-width="4"/></svg></div><p>PR, MARKETING<br><b>&amp;ADVERTISING</b></p></div>
  <div class="service" style="left:730px"><div class="ring"><svg viewBox="0 0 66 66"><circle cx="22" cy="20" r="8" fill="#1e9ad6"/><circle cx="38" cy="20" r="8" fill="#1e9ad6"/><rect x="12" y="28" width="34" height="22" rx="2" fill="#1e9ad6"/><polygon points="46,34 58,28 58,50 46,44" fill="#1e9ad6"/></svg></div><p>EVENTS<br><b>PRODUCTION</b></p></div>
</section>

<h2 class="section-title portfolio-title">PORTFOLIO</h2>
<p class="lead" style="top:1232px;left:325px;width:550px;font-size:11px;line-height:15px">Our portfolio brings together film, live and branded work made with clients who care about craft. Each piece shows the story we told, the way we told it and the results it delivered for the people behind it.</p>

<div class="tile" style="left:0;top:1317px;width:653px;height:277px;background:linear-gradient(120deg,#3a8ccf,#c9a57a 55%,#8a6a4a)" role="img" aria-label="Portfolio: yoga studio campaign"></div>
<div class="tile" style="left:674px;top:1317px;width:251px;height:277px;background:linear-gradient(#d8b768,#8a6a34)" role="img" aria-label="Portfolio: interview portrait"></div>
<div class="tile" style="left:946px;top:1317px;width:254px;height:440px;background:linear-gradient(#f4f4f4,#c9b7a8 60%,#7a2a30)" role="img" aria-label="Portfolio: athlete portrait"></div>
<div class="tile" style="left:0;top:1620px;width:363px;height:168px;background:linear-gradient(120deg,#2a1f6a,#6a3aa0,#1e3a8a)" role="img" aria-label="Portfolio: dance event"></div>
<div class="tile link-tile" style="left:384px;top:1620px;width:269px;height:363px;background:linear-gradient(#1e9ad6,#1779b8)"><span><svg width="44" height="44" viewBox="0 0 44 44"><rect x="6" y="16" width="20" height="12" rx="6" transform="rotate(-45 16 22)" fill="none" stroke="#1e9ad6" stroke-width="4"/><rect x="18" y="16" width="20" height="12" rx="6" transform="rotate(-45 28 22)" fill="none" stroke="#1e9ad6" stroke-width="4"/></svg></span></div>
<div class="tile" style="left:674px;top:1620px;width:251px;height:277px;background:radial-gradient(circle at 40% 30%,#9a9a9a,#1c1c1c 70%)" role="img" aria-label="Portfolio: stage lighting"></div>
<div class="tile" style="left:946px;top:1783px;width:254px;height:420px;background:linear-gradient(#0c0c10,#1c2a4a)" role="img" aria-label="Portfolio: orchestra conductor"></div>
<div class="tile" style="left:0;top:1814px;width:363px;height:182px;background:linear-gradient(120deg,#3a1a10,#b0602a,#2a1a20)" role="img" aria-label="Portfolio: theater bar scene"></div>
<div class="tile" style="left:384px;top:2009px;width:269px;height:194px;background:linear-gradient(#e8dcc0,#b89a6a)" role="img" aria-label="Portfolio: close-up character portrait"></div>
<div class="tile" style="left:674px;top:1918px;width:251px;height:285px;background:linear-gradient(#3a78c0,#2a4a8a)" role="img" aria-label="Portfolio: speaker portrait"></div>
<div class="tile" style="left:0;top:2017px;width:363px;height:186px;background:linear-gradient(120deg,#d8d8d8,#c2202a 50%,#6a6a6a)" role="img" aria-label="Portfolio: sports car showcase"></div>

<section class="press" aria-label="Press">
  <h2 class="section-title">PRESS</h2>
  <p class="lead" style="top:140px;left:320px;width:560px;font-size:11px;line-height:15px">Coverage of our productions in arts and trade publications, from stage reviews to festival features. Read the latest stories about our team, our clients and the work we create together each season.</p>
</section>

<article class="card" style="left:251px;top:2475px;width:371px;height:407px">
  <div style="height:228px;background:linear-gradient(120deg,#3a1a10,#b0602a,#2a1a20)" role="img" aria-label="Theater bar scene"></div>
  <div style="padding:10px">
    <div class="meta"><span>By admin</span><span>&#9643; 1 &nbsp;<em>&#9829; 1</em></span></div>
    <h3><b>28 JUN:</b> PHOTO FEATURED ON RIVERSIDE STAGE ARTS</h3>
    <p>Our production still was chosen to open the review of the season premiere, with notes on lighting, set and the cast that carried the night.</p>
  </div>
  <div class="card-foot"><span class="share"></span><span class="more">Read More</span></div>
</article>

<article class="card" style="left:640px;top:2480px;width:145px;height:190px;padding:8px">
  <div class="meta"><span>By admin</span><em>&#9829; 1</em></div>
  <h3><b>27 JUN:</b> NEW SHOOT WRAPPED</h3>
  <p>A two day shoot for a regional brand closed on time with a full crew and a bold look.</p>
  <div class="card-foot" style="left:8px;right:8px;bottom:8px"><span class="share"></span><span class="more" style="width:70px">Read More</span></div>
</article>
<article class="card" style="left:801px;top:2480px;width:148px;height:190px;padding:8px">
  <div class="meta"><span>By admin</span><em>&#9829; 1</em></div>
  <h3><b>27 JUN:</b> FESTIVAL LINEUP OUT</h3>
  <p>Our short film joins the summer lineup alongside work from local directors and crews.</p>
  <div class="card-foot" style="left:8px;right:8px;bottom:8px"><span class="share"></span><span class="more" style="width:70px">Read More</span></div>
</article>
<article class="card" style="left:640px;top:2690px;width:145px;height:192px;padding:8px">
  <div class="meta"><span>By admin</span><em>&#9829; 1</em></div>
  <h3><b>27 JUN:</b> LIVE EVENT RECAP</h3>
  <p>The gala stage build, sound and video came together for a packed room of guests.</p>
  <div class="card-foot" style="left:8px;right:8px;bottom:8px"><span class="share"></span><span class="more" style="width:70px">Read More</span></div>
</article>
<article class="card" style="left:801px;top:2690px;width:148px;height:192px;padding:8px">
  <div class="meta"><span>By admin</span><em>&#9829; 1</em></div>
  <h3><b>27 JUN:</b> TEAM GROWS AGAIN</h3>
  <p>Two editors and a colorist join the studio to support a busy fall production slate.</p>
  <div class="card-foot" style="left:8px;right:8px;bottom:8px"><span class="share"></span><span class="more" style="width:70px">Read More</span></div>
</article>

<section class="testimonials" aria-label="Testimonials">
  <h2>TESTIMONIALS</h2>
  <div class="avatar" role="img" aria-label="Client portrait"></div>
  <div class="t-name">NORTHLIGHT DOCS FILM FESTIVAL</div>
  <div class="t-role">CEO at Brightway Public Relations</div>
  <p class="t-quote">Orbina is a unique platform that enables us to reach the most accurate media data any time and from anywhere. This provides our team a significant time saving when we distribute content to media and supports our process from time and efficiency perspective.</p>
  <svg class="abs" style="left:584px;top:380px" width="32" height="24"><path d="M2 22V12Q2 2 12 2v5q-4 0-4 5h4v10zM18 22V12q0-10 10-10v5q-4 0-4 5h4v10z" fill="#fff"/></svg>
  <div class="dots"><i class="on"></i><i></i><i></i><i></i></div>
</section>

<section class="newsletter" aria-label="Newsletter">
  <svg class="abs" style="left:186px;top:38px" width="100" height="62"><rect x="2" y="2" width="72" height="50" fill="#fff" stroke="#1e9ad6" stroke-width="3"/><polyline points="2,2 38,30 74,2" fill="none" stroke="#1e9ad6" stroke-width="3"/><polygon points="58,34 82,34 82,26 98,42 82,58 82,50 58,50" fill="#1e9ad6"/></svg>
  <h2>Newletters</h2>
  <div class="nl-input">Your Email Address</div>
  <div class="nl-send">Send</div>
  <div class="nl-social"><i style="background:#3b5998"></i><i style="background:#2aa9e0"></i><i style="background:#f57d00"></i><i style="background:#dd4b39"></i></div>
</section>

<footer class="site-footer">
  <div class="f-col" style="left:251px;width:160px">
    <h4>ABOUT ZANTORVO</h4>
    <p>Zantorvo Media &amp; Entertainment provides full-service campaigns in film and media production, live entertainment and theatrical production, marketing and advertising, and event management in the region. Founded in 2009, the studio has built a strong reputation working for clients across film, music and the arts.</p>
  </div>
  <div class="f-col" style="left:433px;width:170px">
    <h4>CONTACT US</h4>
    <p>Reach our studio team for new projects, press and events.</p>
    <p style="margin-top:8px"><b>Address:</b> 4180 Alder Lane #12, Westbrook, MD 20900</p>
    <p style="margin-top:8px"><b>Phone Number:</b> +1 555 014 2870</p>
    <p style="margin-top:8px"><b>Email:</b> info@zantorvo.com</p>
  </div>
  <div class="f-col" style="left:627px;width:140px">
    <h4>USEFUL LINKS</h4>
    <ul class="f-links"><li>Home</li><li>About us</li><li>Services</li><li>Testimonials</li><li>Blog</li><li>Contact us</li></ul>
  </div>
  <div class="f-col" style="left:788px;width:170px">
    <h4>RECENT POSTS</h4>
    <div class="post"><i></i><span>With Gallery Slider<br>March 18, 2017</span></div>
    <div class="post"><i></i><span>With Gallery Slider<br>March 18, 2017</span></div>
  </div>
</footer>
<div class="copyright">&copy;Copyright 2017 Zantorvo all rights reserved</div>

</body>
</html>
```